Medicinal Cannabis Patient Monitoring App

We have a BASIC design for our app for monitoring patients who received Medicinal Cannabis.
The patient would rate how they're feeling after each dose.

The general flow once user is logged in and set up in the system is:

- User should be able to enter the dosing information for the current day
* Consumption Details:
> Enter Time
> Enter Dosage Taken (Added during onboarding)
> Method take to consume the drug
* Score Details:
> Pain Score (On the scale of 1-10)
> Nausea Score (On the scale of 1-10)
> Sedation Score (On the scale of 1-10)
> Wellbeing Score (On the scale of 1-10)
* Blood Pressure Details:
> Pulse
> Blood Pressure Readings
- User should be able to view the instructions
- User should be able to submit the entered details in the platform

We're looking for a clean, medical and SIMPLE design.

OUR USERS are often ELDERLY, Children and disabled individuals. You must consider this in the design.
So, for example, when designing sliders you should consider a creative way to explain the meaning of the slider if the person cant read the word description.

Designs look the same

```html
<!DOCTYPE html>
<html lang="en">
<head>
<meta charset="utf-8">
<title>Patient Dosing Monitor – Screens</title>
<link href="https://fonts.googleapis.com/css2?family=Poppins:wght@400;500;600;700&display=swap" rel="stylesheet">
<style>
  :root{
    --bg:#23405e;
    --teal:#3aaecd;
    --teal-deep:#2b97ba;
    --teal-dark:#23809f;
    --knob:#2a8db0;
    --ink:#1f2a33;
    --white:#ffffff;
    --line:#e3e7ea;
    --row-hi:#eeeeee;
    --track-bg:#e4e7ea;
  }
  *{box-sizing:border-box;margin:0;padding:0}
  html,body{width:1200px;height:1169px;overflow:hidden}
  body{background:var(--bg);font-family:'Poppins',sans-serif;position:relative}

  .screen{position:absolute;width:320px;overflow:hidden;
    background:linear-gradient(180deg,var(--teal) 0%,var(--teal-deep) 100%);color:var(--white)}
  .screen--phone{left:92px;top:128px;transform:scale(.86);transform-origin:top left;border-radius:26px}
  .screen--drug{left:778px;top:102px;height:566px}
  .screen--feeling{left:428px;top:102px;height:492px}
  .screen--readings{left:428px;top:622px;height:457px}
  .screen--phone{height:566px}

  .skyline{position:absolute;left:0;right:0;
    background:linear-gradient(180deg,rgba(255,255,255,0) 0%,rgba(20,90,120,.18) 55%,rgba(20,90,120,.22) 100%)}
  .waves{position:absolute;left:0;width:320px}
  .base{position:absolute;left:0;right:0;bottom:0;background:var(--white)}

  .heading{position:absolute;left:0;right:0;text-align:center;font-weight:600;letter-spacing:.3px}
  .heading--sm{font-size:15.5px}
  .heading--md{font-size:22px;font-weight:700;letter-spacing:.4px}
  .heading--lg{font-size:24px;font-weight:700;letter-spacing:.5px}

  /* time picker */
  .time-picker{position:absolute;left:18px;top:72px;width:286px;height:182px;background:var(--white);
    border-radius:5px;color:var(--ink);font-size:11px}
  .time-row{position:absolute;left:0;right:0;display:flex;align-items:center;height:27px}
  .time-row.is-selected{background:var(--row-hi);height:39px;box-shadow:0 2px 4px rgba(0,0,0,.12)}
  .time-row span{text-align:center;height:100%;display:flex;align-items:center;justify-content:center;border-right:1px solid var(--line)}
  .time-row span:last-child{border-right:none}
  .c-day{width:114px}.c-hr{width:57px}.c-min{width:50px}.c-ap{width:65px}
  .time-row + .time-row{border-top:1px solid var(--line)}

  .dose-field{position:absolute;left:18px;top:311px;width:286px;height:34px;background:var(--white);border-radius:6px}
  .dose-field i{position:absolute;right:6px;top:6px;width:22px;height:22px;border-radius:50%;background:var(--teal-deep)}

  .methods{position:absolute;left:0;right:0;top:378px}
  .method{position:absolute;width:80px;text-align:center;font-size:11px;font-weight:600;letter-spacing:.3px}
  .method .disc{display:block;width:44px;height:44px;margin:0 auto 8px;border-radius:50%;background:var(--white)}
  .method svg{width:44px;height:44px}

  .btn{position:absolute;height:27px;border-radius:14px;color:var(--white);font-weight:700;font-size:13px;
    letter-spacing:.5px;display:flex;align-items:center;justify-content:center;
    background:linear-gradient(90deg,var(--teal) 0%,var(--teal-dark) 100%);box-shadow:0 2px 4px rgba(0,0,0,.2)}

  /* sliders */
  .score-card{position:absolute;left:17px;width:286px;height:69px;background:var(--white);border-radius:6px;color:var(--ink)}
  .score-card svg{position:absolute;left:0;top:0}
  .score-card .lo,.score-card .hi,.score-card .label{position:absolute;top:40px;font-size:14px}
  .score-card .lo{left:17px}
  .score-card .hi{right:15px}
  .score-card .label{left:0;right:0;text-align:center;font-weight:600;font-size:15px}

  /* readings */
  .reading{position:absolute;left:17px;width:286px;height:32px;background:var(--white);border-radius:16px;
    color:var(--ink);font-size:11px;padding-left:20px;display:flex;align-items:center}
  .upload-note{position:absolute;left:10px;right:10px;top:222px;text-align:center;font-weight:700;
    font-size:15px;line-height:25.6px;letter-spacing:.3px}
</style>
</head>
<body>

<!-- Consumption screen (device view) -->
<section class="screen screen--phone">
  <div class="skyline" role="img" aria-label="Faint city skyline photo behind the form" style="top:250px;height:200px"></div>
  <h2 class="heading heading--sm" style="top:27px">ENTER TIME OF TAKING DRUG</h2>
  <div class="time-picker">
    <div class="time-row" style="top:10px"><span class="c-day">Sun 28 jan</span><span class="c-hr">10</span><span class="c-min">50</span><span class="c-ap"></span></div>
    <div class="time-row" style="top:37px"><span class="c-day">Mon 29 jan</span><span class="c-hr">11</span><span class="c-min">55</span><span class="c-ap"></span></div>
    <div class="time-row is-selected" style="top:68px"><span class="c-day">Today</span><span class="c-hr">12</span><span class="c-min">00</span><span class="c-ap">pm</span></div>
    <div class="time-row" style="top:111px"><span class="c-day">Wed 31 Jan</span><span class="c-hr">1</span><span class="c-min">05</span><span class="c-ap">pm</span></div>
    <div class="time-row" style="top:144px;border-top:none"><span class="c-day">Thu 1 Feb</span><span class="c-hr">3</span><span class="c-min">10</span><span class="c-ap">pm</span></div>
  </div>
  <h2 class="heading heading--sm" style="top:282px">ENTER DOSAGE TAKEN</h2>
  <div class="dose-field"><i></i></div>
  <div class="methods">
    <div class="method" style="left:39px"><span class="disc"><svg viewBox="0 0 44 44"><rect x="15" y="11" width="14" height="21" rx="2" fill="none" stroke="#2b97ba" stroke-width="2.4"/><circle cx="22" cy="28.5" r="1.3" fill="#2b97ba"/></svg></span>TABLET</div>
    <div class="method" style="left:122px"><span class="disc"><svg viewBox="0 0 44 44"><circle cx="22" cy="22" r="19" fill="none" stroke="#2b97ba" stroke-width="2.4"/><line x1="9" y1="9" x2="35" y2="35" stroke="#2b97ba" stroke-width="2.4"/><rect x="12" y="24" width="18" height="4" fill="#2b97ba"/><path d="M24 12c3 2 0 5 3 7" fill="none" stroke="#2b97ba" stroke-width="2"/></svg></span>SMOKE</div>
    <div class="method" style="left:206px"><span class="disc"><svg viewBox="0 0 44 44"><rect x="18" y="16" width="8" height="18" rx="1.5" fill="#2b97ba"/><rect x="20" y="9" width="4" height="7" fill="#2b97ba"/></svg></span>VAPE</div>
  </div>
  <svg class="waves" style="top:448px" width="320" height="80" viewBox="0 0 320 80" aria-hidden="true">
    <path d="M0 40 C60 10 110 10 170 30 S280 40 320 20 V80 H0Z" fill="#9fd8e8" opacity=".7"/>
    <path d="M0 55 C70 25 140 25 200 42 S290 55 320 45 V80 H0Z" fill="#d6eff6"/>
    <path d="M0 68 C80 52 170 60 320 62 V80 H0Z" fill="#f4fbfd"/>
  </svg>
  <div class="base" style="height:40px"></div>
  <div class="btn" style="left:144px;top:523px;width:90px">NEXT</div>
</section>

<!-- Score screen -->
<section class="screen screen--feeling">
  <div class="skyline" role="img" aria-label="Faint city skyline photo behind the sliders" style="top:300px;height:160px"></div>
  <h2 class="heading heading--md" style="top:24px">How are you feeling?</h2>

  <div class="score-card" style="top:81px">
    <svg width="286" height="40" viewBox="0 0 286 40" aria-hidden="true"><rect x="10" y="17" width="266" height="14" rx="7" fill="var(--track-bg)"/><rect x="22" y="22" width="246" height="4" fill="var(--teal-deep)"/><g stroke="#9aa3a8" stroke-width="1"><line x1="65" y1="15" x2="65" y2="33"/><line x1="108" y1="15" x2="108" y2="33"/><line x1="159" y1="15" x2="159" y2="33"/><line x1="210" y1="15" x2="210" y2="33"/></g><circle cx="22" cy="24" r="7" fill="var(--knob)" stroke="#9cd3e3" stroke-width="2"/><circle cx="268" cy="24" r="7" fill="var(--knob)" stroke="#9cd3e3" stroke-width="2"/></svg>
    <span class="lo">1</span><span class="label">Pain</span><span class="hi">10</span>
  </div>
  <div class="score-card" style="top:164px">
    <svg width="286" height="40" viewBox="0 0 286 40" aria-hidden="true"><rect x="10" y="17" width="266" height="14" rx="7" fill="var(--track-bg)"/><rect x="22" y="22" width="246" height="4" fill="var(--teal-deep)"/><g stroke="#9aa3a8" stroke-width="1"><line x1="65" y1="15" x2="65" y2="33"/><line x1="108" y1="15" x2="108" y2="33"/><line x1="159" y1="15" x2="159" y2="33"/><line x1="210" y1="15" x2="210" y2="33"/></g><circle cx="22" cy="24" r="7" fill="var(--knob)" stroke="#9cd3e3" stroke-width="2"/><circle cx="268" cy="24" r="7" fill="var(--knob)" stroke="#9cd3e3" stroke-width="2"/></svg>
    <span class="lo">1</span><span class="label">Nausea</span><span class="hi">10</span>
  </div>
  <div class="score-card" style="top:247px">
    <svg width="286" height="40" viewBox="0 0 286 40" aria-hidden="true"><rect x="10" y="17" width="266" height="14" rx="7" fill="var(--track-bg)"/><rect x="22" y="22" width="246" height="4" fill="var(--teal-deep)"/><g stroke="#9aa3a8" stroke-width="1"><line x1="65" y1="15" x2="65" y2="33"/><line x1="108" y1="15" x2="108" y2="33"/><line x1="159" y1="15" x2="159" y2="33"/><line x1="210" y1="15" x2="210" y2="33"/></g><circle cx="22" cy="24" r="7" fill="var(--knob)" stroke="#9cd3e3" stroke-width="2"/><circle cx="268" cy="24" r="7" fill="var(--knob)" stroke="#9cd3e3" stroke-width="2"/></svg>
    <span class="lo">1</span><span class="label">Sedation</span><span class="hi">10</span>
  </div>
  <div class="score-card" style="top:330px">
    <svg width="286" height="40" viewBox="0 0 286 40" aria-hidden="true"><rect x="10" y="17" width="266" height="14" rx="7" fill="var(--track-bg)"/><rect x="22" y="22" width="246" height="4" fill="var(--teal-deep)"/><g stroke="#9aa3a8" stroke-width="1"><line x1="65" y1="15" x2="65" y2="33"/><line x1="108" y1="15" x2="108" y2="33"/><line x1="159" y1="15" x2="159" y2="33"/><line x1="210" y1="15" x2="210" y2="33"/></g><circle cx="22" cy="24" r="7" fill="var(--knob)" stroke="#9cd3e3" stroke-width="2"/><circle cx="268" cy="24" r="7" fill="var(--knob)" stroke="#9cd3e3" stroke-width="2"/></svg>
    <span class="lo">1</span><span class="label">Wellbeing</span><span class="hi">10</span>
  </div>

  <svg class="waves" style="top:420px" width="320" height="50" viewBox="0 0 320 50" aria-hidden="true">
    <path d="M0 40 C60 20 110 5 170 12 S270 30 320 30 V50 H0Z" fill="#b9e3ef" opacity=".8"/>
    <path d="M0 45 C80 30 160 30 240 38 S300 42 320 40 V50 H0Z" fill="#e3f4f9"/>
  </svg>
  <div class="base" style="height:30px"></div>
</section>

<!-- Readings screen -->
<section class="screen screen--readings">
  <div class="skyline" role="img" aria-label="Faint city skyline photo behind the readings form" style="top:200px;height:190px"></div>
  <h2 class="heading heading--lg" style="top:47px">READINGS</h2>
  <div class="reading" style="top:110px">PULSE</div>
  <div class="reading" style="top:164px">BLOOD PRESSURE</div>
  <p class="upload-note">THESE ARE NOW BEING<br>UPLOADED TO THE CONFIDENTIAL<br>DATA BASE</p>
  <svg class="waves" style="top:355px" width="320" height="70" viewBox="0 0 320 70" aria-hidden="true">
    <path d="M0 40 C60 15 120 0 180 8 S280 30 320 25 V70 H0Z" fill="#a9dcec" opacity=".8"/>
    <path d="M0 52 C70 35 150 32 220 40 S300 48 320 44 V70 H0Z" fill="#dff2f8"/>
    <path d="M0 62 C90 55 200 58 320 58 V70 H0Z" fill="#f6fcfd"/>
  </svg>
  <div class="base" style="height:40px"></div>
  <div class="btn" style="left:115px;top:417px;width:90px">SUBMIT</div>
</section>

<!-- Consumption screen (flat) -->
<section class="screen screen--drug">
  <div class="skyline" role="img" aria-label="Faint city skyline photo behind the form" style="top:250px;height:210px"></div>
  <h2 class="heading heading--sm" style="top:27px">ENTER TIME OF TAKING DRUG</h2>
  <div class="time-picker">
    <div class="time-row" style="top:10px"><span class="c-day">Sun 28 jan</span><span class="c-hr">10</span><span class="c-min">50</span><span class="c-ap"></span></div>
    <div class="time-row" style="top:37px"><span class="c-day">Mon 29 jan</span><span class="c-hr">11</span><span class="c-min">55</span><span class="c-ap"></span></div>
    <div class="time-row is-selected" style="top:68px"><span class="c-day">Today</span><span class="c-hr">12</span><span class="c-min">00</span><span class="c-ap">pm</span></div>
    <div class="time-row" style="top:111px"><span class="c-day">Wed 31 Jan</span><span class="c-hr">1</span><span class="c-min">05</span><span class="c-ap">pm</span></div>
    <div class="time-row" style="top:144px;border-top:none"><span class="c-day">Thu 1 Feb</span><span class="c-hr">3</span><span class="c-min">10</span><span class="c-ap">pm</span></div>
  </div>
  <h2 class="heading heading--sm" style="top:278px">ENTER DOSAGE TAKEN</h2>
  <div class="dose-field"><i></i></div>
  <div class="methods">
    <div class="method" style="left:39px"><span class="disc"><svg viewBox="0 0 44 44"><rect x="15" y="11" width="14" height="21" rx="2" fill="none" stroke="#2b97ba" stroke-width="2.4"/><circle cx="22" cy="28.5" r="1.3" fill="#2b97ba"/></svg></span>TABLET</div>
    <div class="method" style="left:122px"><span class="disc"><svg viewBox="0 0 44 44"><circle cx="22" cy="22" r="19" fill="none" stroke="#2b97ba" stroke-width="2.4"/><line x1="9" y1="9" x2="35" y2="35" stroke="#2b97ba" stroke-width="2.4"/><rect x="12" y="24" width="18" height="4" fill="#2b97ba"/><path d="M24 12c3 2 0 5 3 7" fill="none" stroke="#2b97ba" stroke-width="2"/></svg></span>SMOKE</div>
    <div class="method" style="left:206px"><span class="disc"><svg viewBox="0 0 44 44"><rect x="18" y="16" width="8" height="18" rx="1.5" fill="#2b97ba"/><rect x="20" y="9" width="4" height="7" fill="#2b97ba"/></svg></span>VAPE</div>
  </div>
  <svg class="waves" style="top:448px" width="320" height="80" viewBox="0 0 320 80" aria-hidden="true">
    <path d="M0 40 C60 10 110 10 170 30 S280 40 320 20 V80 H0Z" fill="#9fd8e8" opacity=".7"/>
    <path d="M0 55 C70 25 140 25 200 42 S290 55 320 45 V80 H0Z" fill="#d6eff6"/>
    <path d="M0 68 C80 52 170 60 320 62 V80 H0Z" fill="#f4fbfd"/>
  </svg>
  <div class="base" style="height:40px"></div>
  <div class="btn" style="left:115px;top:523px;width:90px">NEXT</div>
</section>

</body>
</html>
```